Wade Merriton Professional Coaching

I would like a website with a mountain theme geared towards professional executives reaching higher peaks and goals. This is a 3 page website with brand essence information on the opening page, the coaching process on a second page and "about me" and lead capture form on a third page

Target Market(s)

C-Level audience, involved in tech, government, manufacturing, and transportation type of corporations

Coding

Number of Pages Required

3 page

Font styles to use
Sans Serif

Colors
a7a7a7
1b1b1b
e8e8e8
3176b5
abd036
0355a3

Requirements
Must have
• Looking for a user friendly site that I can manage/update going forward. Must have:
• 1. "Is coaching right for you?" - page 1
• 2. "Our Process" page 2 - I will describe how we approach coaching
• 3. "Contact us" page 3 where I can capture contact information from potential clients
• 4. Clean and professional with more modern font
• 5. Links to personal social media sites
• 6. Ability to upload/download .pdf documents as resources
• 7. Ability to add on new pages in the future (such as a blog page)
Nice to have
• I want a place to store articles I write or use.
• Profile or Twitter Feed
Should not have
• Not fluffy or too 'zen' like personal life coaches tend to present.

```html
<!DOCTYPE html>
<html lang="en">
<head>
<meta charset="utf-8">
<title>Wade Merriton Performance Coaching</title>
<link href="https://fonts.googleapis.com/css2?family=Poppins:wght@300;400;500;600&display=swap" rel="stylesheet">
<style>
:root{
  --navy:#0d1f3c;
  --gold:#a48a56;
  --bronze:#9a7e4b;
  --ink:#1b1b1b;
  --text:#555;
  --muted:#8a8a8a;
  --line:#e8e8e8;
  --footer:#8f8c87;
  --white:#fff;
}
*{box-sizing:border-box;margin:0;padding:0}
html,body{width:1200px;height:2866px;overflow:hidden;background:var(--white)}
body{position:relative;font-family:'Poppins',sans-serif;color:var(--ink)}
.abs{position:absolute}
a{color:inherit;text-decoration:none}

/* header */
.site-header{left:0;top:0;width:1200px;height:71px;border-bottom:1px solid var(--line);background:var(--white)}
.menu-toggle{left:22px;top:28px;width:16px}
.menu-toggle span{display:block;height:2px;background:var(--ink);margin-bottom:4px}
.header-divider{top:0;width:1px;height:71px;background:var(--line)}
.main-nav{left:82px;top:0;display:flex;gap:22px;font-size:11px;text-transform:uppercase;height:71px;align-items:center}
.main-nav a{height:71px;line-height:71px}
.main-nav .active{color:var(--gold);border-bottom:2px solid var(--gold)}
.brand{left:500px;top:0;width:200px;height:71px;display:flex;align-items:center;justify-content:center;gap:8px}
.brand-mark{width:8px;height:8px;background:var(--ink)}
.brand-name{font-size:18px;font-weight:400;letter-spacing:.5px;white-space:nowrap}
.header-phone{left:878px;top:27px;font-size:11px;color:var(--text);display:flex;align-items:center;gap:8px;white-space:nowrap}
.header-search{left:1041px;top:27px}
.btn{background:var(--navy);color:var(--white);font-size:10px;font-weight:500;display:flex;align-items:center;justify-content:space-between;padding:0 0 0 14px;white-space:nowrap}
.btn::after{content:"›";font-size:15px;width:30px;justify-content:center;border-left:1px solid rgba(255,255,255,.25);height:100%;display:flex;align-items:center}
.header-cta{left:1069px;top:19px;width:112px;height:33px}

/* hero */
.hero{left:0;top:71px;width:1200px;height:487px;background:linear-gradient(180deg,#d8e6f2 0%,#a9c8e6 40%,#5f9bd6 70%,#8bb6e1 100%)}
.hero-title{left:235px;top:250px;color:var(--white);font-weight:300;font-size:46px;line-height:48px;text-transform:uppercase;white-space:nowrap}
.hero-sub{left:237px;top:357px;color:var(--white);font-size:10px;line-height:14px;width:170px}
.hero-badge{left:828px;top:268px;width:64px;height:68px;border:5px solid var(--white)}
.hero-badge-text{left:848px;top:280px;color:rgba(255,255,255,.85);font-size:7px;line-height:9px;width:80px;text-transform:uppercase}
.hero-arrow{top:290px;color:var(--white);font-size:40px;font-weight:300}
.hero-dots{left:578px;top:464px;display:flex;gap:8px}
.hero-dots span{width:8px;height:8px;border-radius:50%;background:rgba(255,255,255,.55)}
.hero-dots span:first-child{background:var(--white)}

/* profile */
.profile-tab{left:237px;top:460px;width:120px;height:39px;background:var(--white);font-size:10px;display:flex;align-items:center;gap:6px;padding-left:10px;border:1px solid var(--line);border-bottom:0;white-space:nowrap}
.profile-tab b{font-weight:600}
.profile-tab i{width:8px;height:8px;background:var(--gold);display:inline-block}
.profile-card{left:237px;top:499px;width:728px;height:424px;background:var(--white);box-shadow:0 1px 0 var(--line)}
.profile-photo{left:0;top:0;width:363px;height:424px;background:linear-gradient(135deg,#6f8f4f 0%,#3b5a2e 45%,#25324f 75%,#7d6a57 100%)}
.profile-name{left:405px;top:95px;font-size:35px;font-weight:300;text-transform:uppercase;white-space:nowrap}
.profile-role{left:405px;top:144px;width:260px;font-size:13px;line-height:21px;color:var(--muted)}
.profile-loc{left:405px;top:245px;font-size:9px;color:var(--text);white-space:nowrap}
.profile-cta{left:405px;top:289px;width:165px;height:33px}

.reasons-label{left:237px;top:940px;font-size:9px}
.reasons{left:237px;top:960px;width:728px;display:flex;justify-content:space-between}
.reason{display:flex;align-items:center;gap:12px;font-size:9px;line-height:12px;color:var(--text);text-transform:uppercase;width:160px}
.tick{width:30px;height:30px;flex:none}
.rule{height:1px;background:var(--line)}

/* section headings */
.section-title{width:1200px;left:0;text-align:center;font-size:18px;font-weight:300;text-transform:uppercase}
.title-line{display:block;width:34px;height:1px;background:var(--ink);margin:0 auto 8px}
.process-text{left:300px;top:1146px;width:600px;text-align:center;font-size:11px;line-height:20px;color:var(--text)}

/* photo band + quote */
.office-photo{left:0;top:1246px;width:1200px;height:449px;background:linear-gradient(90deg,#6a6a6a 0%,#bdbdbd 35%,#9a9a9a 60%,#2e2e2e 80%,#d0d0d0 100%)}
.exec-panel{left:237px;top:1634px;width:363px;height:424px;background:var(--bronze);color:var(--white);text-align:center}
.exec-line{width:80px;height:2px;background:var(--white);margin:130px auto 0}
.exec-title{margin-top:22px;font-size:22px;font-weight:300;line-height:27px;text-transform:uppercase}
.exec-text{margin:22px auto 0;width:190px;font-size:10px;line-height:16px}
.quote-form{left:600px;top:1634px;width:365px;height:424px;background:var(--white);border-bottom:1px solid var(--line);padding:42px 44px}
.quote-form h3{font-size:11px;font-weight:600;margin-bottom:24px}
.field{margin-bottom:18px;width:278px}
.field label{display:block;font-size:10px;margin-bottom:6px}
.field .input{font-size:12px;color:var(--muted);border-bottom:1px solid var(--gold);padding-bottom:8px;display:flex;justify-content:space-between;align-items:center}
.field .select{color:var(--gold)}
.extra-line{width:278px;height:1px;background:var(--gold);margin:18px 0 28px}
.submit{width:165px;height:33px}

/* articles */
.article-card{top:2173px;width:226px;height:231px;border-bottom:2px solid var(--line);text-align:center}
.article-img{width:226px;height:150px}
.article-card h4{margin-top:14px;font-size:15px;font-weight:300;text-transform:uppercase;white-space:nowrap}
.article-card p{margin:6px auto 0;width:190px;font-size:9px;line-height:13px;color:var(--text)}
.slider-arrow{top:2245px;font-size:46px;font-weight:200;color:var(--ink)}
.view-all{left:518px;top:2429px;width:164px;height:33px}
.to-top{left:1089px;top:2500px;width:39px;height:38px;background:#000;display:flex;align-items:center;justify-content:center;z-index:2}

/* footer */
.site-footer{left:0;top:2523px;width:1200px;height:343px;background:var(--footer);color:var(--white)}
.join-title{left:222px;top:48px;font-size:17px;font-weight:300;text-transform:uppercase;white-space:nowrap}
.join-text{left:438px;top:43px;width:240px;font-size:9px;line-height:15px}
.join-input{left:703px;top:36px;width:242px;height:42px;background:var(--white);color:var(--text);font-size:10px;display:flex;align-items:center;justify-content:space-between;padding:0 16px}
.footer-rule{left:160px;top:99px;width:880px;height:1px;background:rgba(255,255,255,.3)}
.f-col{top:144px;font-size:9px;line-height:16px;white-space:nowrap}
.f-col h5{font-size:10px;font-weight:600;text-transform:uppercase;margin-bottom:14px}
.socials{display:grid;grid-template-columns:repeat(3,26px);gap:18px 14px}
.social{width:26px;height:26px;background:var(--white);display:flex;align-items:center;justify-content:center}
.social i{width:8px;height:8px;border-radius:50%;background:var(--footer)}
.contact-line{display:flex;align-items:center;gap:8px;margin-top:8px}
.footer-cta{left:874px;top:146px;width:166px;height:32px;border:1px solid var(--white);background:transparent}
.copyright{left:874px;top:193px;font-size:9px;line-height:14px}
</style>
</head>
<body>

<header class="site-header abs">
  <div class="menu-toggle abs"><span></span><span></span><span></span></div>
  <div class="header-divider abs" style="left:60px"></div>
  <nav class="main-nav abs">
    <a class="active" href="#">Home</a><a href="#">About Me</a><a href="#">Coaching Process</a>
  </nav>
  <a class="brand abs" href="#"><span class="brand-mark"></span><span class="brand-name">WADE MERRITON</span></a>
  <div class="header-phone abs">
    <svg width="18" height="18" viewBox="0 0 18 18"><rect x=".5" y=".5" width="17" height="17" fill="none" stroke="#a48a56"/><path d="M5 4l2 0 1 3-1.5 1a6 6 0 0 0 3 3l1-1.5 3 1 0 2c-5 1-9-3-8.5-8.5z" fill="#a48a56"/></svg>
    TEL: (08) 40 5512 3390
  </div>
  <div class="header-divider abs" style="left:1030px"></div>
  <svg class="header-search abs" width="16" height="16" viewBox="0 0 16 16"><circle cx="6.5" cy="6.5" r="5" fill="none" stroke="#555" stroke-width="1.4"/><line x1="10.3" y1="10.3" x2="15" y2="15" stroke="#555" stroke-width="1.4"/></svg>
  <a class="btn header-cta abs" href="#">Talk To Expert</a>
</header>

<section class="hero abs" role="img" aria-label="Misty blue mountain ranges under a pale sky"></section>
<div class="hero-arrow abs" style="left:28px">‹</div>
<div class="hero-arrow abs" style="left:1144px">›</div>
<h1 class="hero-title abs">Reaching Higher<br>Peaks and Goals</h1>
<p class="hero-sub abs">Help individuals achieve their personal and career goals</p>
<div class="hero-badge abs"></div>
<p class="hero-badge-text abs">Reaching<br>higher peaks<br>and goals</p>
<div class="hero-dots abs"><span></span><span></span><span></span></div>

<div class="profile-tab abs"><i></i><b>Profile</b> <span style="color:var(--gold)">View Profile</span></div>
<section class="profile-card abs">
  <div class="profile-photo abs" role="img" aria-label="Portrait of the coach in a navy blazer outdoors"></div>
  <h2 class="profile-name abs">Wade Merriton</h2>
  <p class="profile-role abs">Professionally Certified Executive Coach/Senior Consultant for Leadership, Strategic Thinking, Strategy and Execution</p>
  <p class="profile-loc abs">Greater Summit Area / Professional Training &amp; Coaching</p>
  <a class="btn profile-cta abs" href="#">Meet Him Today</a>
</section>

<p class="reasons-label abs">4 Reasons To Join Wade Merriton</p>
<div class="reasons abs">
  <div class="reason"><svg class="tick" viewBox="0 0 30 30"><circle cx="15" cy="15" r="14" fill="none" stroke="#a48a56" stroke-width="1.4"/><polyline points="9,15 13.5,19.5 21,11" fill="none" stroke="#a48a56" stroke-width="1.6"/></svg>Convenient and<br>affordable</div>
  <div class="reason"><svg class="tick" viewBox="0 0 30 30"><circle cx="15" cy="15" r="14" fill="none" stroke="#a48a56" stroke-width="1.4"/><polyline points="9,15 13.5,19.5 21,11" fill="none" stroke="#a48a56" stroke-width="1.6"/></svg>Certified life coach<br>for individuals</div>
  <div class="reason"><svg class="tick" viewBox="0 0 30 30"><circle cx="15" cy="15" r="14" fill="none" stroke="#a48a56" stroke-width="1.4"/><polyline points="9,15 13.5,19.5 21,11" fill="none" stroke="#a48a56" stroke-width="1.6"/></svg>Certified executive<br>coach for individuals</div>
  <div class="reason"><svg class="tick" viewBox="0 0 30 30"><circle cx="15" cy="15" r="14" fill="none" stroke="#a48a56" stroke-width="1.4"/><polyline points="9,15 13.5,19.5 21,11" fill="none" stroke="#a48a56" stroke-width="1.6"/></svg>Practical coaching<br>training for all</div>
</div>
<div class="rule abs" style="left:237px;top:1026px;width:728px"></div>

<h2 class="section-title abs" style="top:1096px"><span class="title-line"></span>Coaching Process</h2>
<p class="process-text abs">Use of technology for enrollment as well as program delivery enables us to keep our fees low and allows you to take all your classes from the convenience of your home. All you need is an internet connection.</p>

<div class="office-photo abs" role="img" aria-label="Black and white photo of a smiling executive reading at his office desk"></div>

<section class="exec-panel abs">
  <div class="exec-line"></div>
  <h2 class="exec-title">Executive Leaders<br>and Teams</h2>
  <p class="exec-text">Professionally Certified Executive Coach/Senior Consultant for Leadership, Strategic Thinking, Strategy and Execution</p>
</section>
<form class="quote-form abs">
  <h3>GET A QUOTE</h3>
  <div class="field"><label>Full Name</label><div class="input">Enter Name</div></div>
  <div class="field"><label>Email</label><div class="input">Enter Email</div></div>
  <div class="field"><label>Subject</label><div class="input select">Select here <svg width="10" height="6" viewBox="0 0 10 6"><polyline points="1,1 5,5 9,1" fill="none" stroke="#a48a56"/></svg></div></div>
  <div class="field"><label>Message</label><div class="input">Enter here</div></div>
  <div class="extra-line"></div>
  <div class="btn submit">Submit</div>
</form>

<h2 class="section-title abs" style="top:2124px"><span class="title-line"></span>Articles</h2>
<div class="slider-arrow abs" style="left:160px">‹</div>
<div class="slider-arrow abs" style="left:1018px">›</div>
<article class="article-card abs" style="left:237px">
  <div class="article-img" role="img" aria-label="Two people discussing at a whiteboard" style="background:linear-gradient(135deg,#e9e4df,#8a8f99 60%,#5a3b36)"></div>
  <h4>Life Coaching</h4><p>Specialises in supplying wall and floor tiles, mosaics and natural stone</p>
</article>
<article class="article-card abs" style="left:487px">
  <div class="article-img" role="img" aria-label="Hands working at a laptop on a bright desk" style="background:linear-gradient(135deg,#f3ece3,#d9c9b5 55%,#8d8680)"></div>
  <h4>Professional Executives</h4><p>Specialises in supplying wall and floor tiles, mosaics and natural stone</p>
</article>
<article class="article-card abs" style="left:740px">
  <div class="article-img" role="img" aria-label="Businesswoman working at a laptop in a bright office" style="background:linear-gradient(135deg,#f1f1f1,#d8d4d2 50%,#c23b4f)"></div>
  <h4>Executive Leaders</h4><p>Specialises in supplying wall and floor tiles, mosaics and natural stone</p>
</article>
<a class="btn view-all abs" href="#">View All</a>
<a class="to-top abs" href="#"><svg width="18" height="12" viewBox="0 0 18 12"><polyline points="2,10 9,3 16,10" fill="none" stroke="#fff" stroke-width="2.4"/></svg></a>

<footer class="site-footer abs">
  <h3 class="join-title abs">Join Wade Merriton</h3>
  <p class="join-text abs">If you'd like to be kept informed of our special offers and latest news, enter your details below</p>
  <div class="join-input abs">Enter Email <svg width="14" height="10" viewBox="0 0 14 10"><rect x=".5" y=".5" width="13" height="9" fill="none" stroke="#8a8a8a"/><polyline points=".5,.5 7,6 13.5,.5" fill="none" stroke="#8a8a8a"/></svg></div>
  <div class="footer-rule abs"></div>

  <div class="f-col abs" style="left:160px">
    <h5>Social</h5>
    <div class="socials">
      <span class="social"><i></i></span><span class="social"><i></i></span><span class="social"><i></i></span>
      <span class="social"><i></i></span><span class="social"><i></i></span>
    </div>
  </div>
  <div class="f-col abs" style="left:348px">
    <h5>Contact</h5>
    <p>North Ridge Bld. 12,<br>Summit City 4100,<br>Upper Township</p>
    <div class="contact-line" style="margin-top:14px"><svg width="16" height="16" viewBox="0 0 16 16"><rect x=".5" y=".5" width="15" height="15" fill="none" stroke="#fff"/><path d="M4.5 3.5h2l1 2.5-1.3 1a5 5 0 0 0 2.8 2.8l1-1.3 2.5 1v2c-4.5.8-8.5-3-8-8z" fill="#fff"/></svg>T: Tel: (011) 40 5512 3390</div>
    <div class="contact-line"><svg width="16" height="16" viewBox="0 0 16 16"><rect x=".5" y=".5" width="15" height="15" fill="none" stroke="#fff"/><rect x="3.5" y="5" width="9" height="6" fill="none" stroke="#fff"/><polyline points="3.5,5 8,8.5 12.5,5" fill="none" stroke="#fff"/></svg>E: info@wademerriton.com</div>
  </div>
  <div class="f-col abs" style="left:551px">
    <h5>Sitemap</h5>
    <p>Home<br>Coaching Process<br>About Me<br>Articles<br>Contact</p>
  </div>
  <div class="f-col abs" style="left:702px">
    <h5>Services</h5>
    <p>Life Coaching<br>Executive Coaching<br>Executive Leaders and Teams<br>Professional Executives<br>Higher Peaks and Goals</p>
  </div>
  <a class="btn footer-cta abs" href="#">Talk To Expert</a>
  <p class="copyright abs">© 2016 Wade Merriton<br>All Rights Reserved</p>
</footer>

</body>
</html>
```